The Harlow Law Firm, PC

Dwight K. Harlow
Attorney at Law
physical address: 287 E. 9th Avenue
Greenville, NC 27019

mailing: P.O. Box 5843
Greenville, NC 27021

o. 555.416.2071
f. 555.416.8532

www.harlowlegal-ex.com

Industry/Entity Type

Attorney

Contact Information for Business Card

Attorney name
Office Phone number
Office Fax number
Mailing address and physical address
website address

Requirements
Must have
• Clean fresh design - I hate the website

```html
<!DOCTYPE html>
<html lang="en">
<head>
<meta charset="utf-8">
<title>The Harlow Law Firm, PC – Stationery</title>
<link rel="stylesheet" href="https://fonts.googleapis.com/css2?family=Roboto+Condensed:wght@700&family=Arimo:wght@400&display=swap">
<style>
  :root {
    --ink: #4a4137;
    --card: #4a4137;
    --card-text: #f4f0ea;
    --card-art: #6b6157;
    --paper: #ffffff;
    --faint: #f3f0ec;
    --art: #d9d3cc;
    --frame: #222222;
    --label: #222222;
  }
  * { box-sizing: border-box; margin: 0; padding: 0; }
  html, body { width: 1200px; height: 702px; overflow: hidden; background: var(--paper); }
  .board { position: relative; width: 1200px; height: 702px; font-family: "Arimo", Arial, sans-serif; }
  .board p, .board div { white-space: nowrap; }

  .firm-name, .web, .person, .phones, .head {
    font-family: "Roboto Condensed", "Arial Narrow", sans-serif; font-weight: 700;
  }

  /* Letterhead */
  .letterhead { position: absolute; left: 8px; top: 4px; width: 532px; height: 692px; border: 2px solid var(--frame); color: var(--ink); }
  .letterhead > * { position: absolute; }
  .letterhead .firm-name { left: 24px; top: 34px; font-size: 24px; line-height: 1; }
  .letterhead .book-art { left: 284px; top: 20px; width: 100px; height: 44px; background: var(--art); }
  .letterhead .web { left: 24px; top: 122px; font-size: 13px; }
  .letterhead .addresses { right: 22px; top: 28px; text-align: right; font-size: 10.5px; line-height: 1.35; }
  .letterhead .addresses .head { font-size: 12px; }
  .letterhead .addresses .gap { margin-top: 6px; }
  .letterhead .phones { margin-top: 4px; font-size: 12px; letter-spacing: .5px; }
  .letterhead .backdrop { left: 52px; top: 236px; width: 410px; height: 360px; background: var(--faint); }

  /* Labels */
  .label { position: absolute; font-size: 17px; color: var(--label); }
  .label.front { left: 656px; top: 112px; }
  .label.back { left: 980px; top: 302px; }

  /* Cards */
  .card { position: absolute; width: 316px; height: 178px; background: var(--card); color: var(--card-text); font-size: 10.5px; }
  .card > * { position: absolute; line-height: 1; }
  .card .firm-name { left: 12px; font-size: 11.5px; }
  .card .book-art { left: 136px; width: 32px; height: 20px; background: var(--card-art); }
  .card .web { font-size: 11.5px; }
  .card .person { left: 12px; font-size: 15px; letter-spacing: 1.5px; }
  .card .title { left: 12px; font-size: 10.5px; }
  .card .phone { left: 190px; font-family: "Roboto Condensed", sans-serif; font-weight: 700; font-size: 12px; letter-spacing: 1px; }
  .card .addr { left: 12px; }

  .card.one { left: 548px; top: 146px; }
  .card.two { left: 548px; top: 334px; }
  .card.three { left: 548px; top: 520px; }
  .card.reverse { left: 874px; top: 334px; }
  .card.reverse .firm-name { left: 12px; top: 32px; font-size: 20px; }
  .card.reverse .book-art { left: 150px; top: 70px; width: 140px; height: 60px; }
  .card.reverse .web { right: 12px; bottom: 12px; font-size: 12px; }
</style>
</head>
<body>
<main class="board">

  <section class="letterhead" aria-label="Letterhead">
    <div class="firm-name">The Harlow Law Firm, PC</div>
    <div class="book-art" role="img" aria-label="Open law book illustration"></div>
    <div class="web">www.harlowlegal-ex.com</div>
    <div class="addresses">
      <p class="head">Office Address:</p>
      <p>287 E. 9th Avenue</p>
      <p>Greenville, NC 27019</p>
      <p class="head gap">Mailing Address:</p>
      <p>P.O. Box 5843</p>
      <p>Greenville, NC 27021</p>
      <div class="phones">
        <p>o.&nbsp; 555.416.2071</p>
        <p>f.&nbsp; 555.416.8532</p>
      </div>
    </div>
    <div class="backdrop" role="img" aria-label="Faint large firm wordmark background"></div>
  </section>

  <p class="label front">Front Side</p>
  <p class="label back">Back Side</p>

  <article class="card one" aria-label="Business card front, layout one">
    <div class="firm-name" style="top:22px;">The Harlow Law Firm, PC</div>
    <div class="book-art" style="top:18px;" role="img" aria-label="Open law book illustration"></div>
    <div class="web" style="right:12px;top:44px;">www.harlowlegal-ex.com</div>
    <div class="person" style="top:64px;">Dwight K. Harlow</div>
    <div class="title" style="top:82px;">Attorney at Law</div>
    <div class="phone" style="top:64px;">o.&nbsp; 555.416.2071</div>
    <div class="phone" style="top:82px;">f.&nbsp;&nbsp; 555.416.8532</div>
    <div class="addr" style="top:111px;">Mailing Address: P.O. Box 5843</div>
    <div class="addr" style="top:127px;">Greenville, NC 27021</div>
    <div class="addr" style="top:147px;">Office Address: 287 E. 9th Avenue</div>
    <div class="addr" style="top:163px;">Greenville, NC 27019</div>
  </article>

  <article class="card two" aria-label="Business card front, layout two">
    <div class="person" style="top:10px;">Dwight K. Harlow</div>
    <div class="title" style="top:29px;">Attorney at Law</div>
    <div class="phone" style="top:10px;">o.&nbsp; 555.416.2071</div>
    <div class="phone" style="top:28px;">f.&nbsp;&nbsp; 555.416.8532</div>
    <div class="firm-name" style="top:60px;">The Harlow Law Firm, PC</div>
    <div class="book-art" style="top:56px;" role="img" aria-label="Open law book illustration"></div>
    <div class="web" style="right:12px;top:82px;">www.harlowlegal-ex.com</div>
    <div class="addr" style="top:111px;">Mailing Address: P.O. Box 5843</div>
    <div class="addr" style="top:127px;">Greenville, NC 27021</div>
    <div class="addr" style="top:147px;">Office Address: 287 E. 9th Avenue</div>
    <div class="addr" style="top:163px;">Greenville, NC 27019</div>
  </article>

  <article class="card three" aria-label="Business card front, layout three">
    <div class="person" style="top:10px;">Dwight K. Harlow</div>
    <div class="title" style="top:29px;">Attorney at Law</div>
    <div class="phone" style="top:10px;">o.&nbsp; 555.416.2071</div>
    <div class="phone" style="top:28px;">f.&nbsp;&nbsp; 555.416.8532</div>
    <div class="web" style="left:12px;top:80px;">www.harlowlegal-ex.com</div>
    <div class="addr" style="top:111px;">Mailing Address: P.O. Box 5843</div>
    <div class="addr" style="top:127px;">Greenville, NC 27021</div>
    <div class="addr" style="top:147px;">Office Address: 287 E. 9th Avenue</div>
    <div class="addr" style="top:163px;">Greenville, NC 27019</div>
  </article>

  <article class="card reverse" aria-label="Business card back">
    <div class="firm-name">The Harlow Law Firm, PC</div>
    <div class="book-art" role="img" aria-label="Open law book illustration"></div>
    <div class="web">www.harlowlegal-ex.com</div>
  </article>

</main>
</body>
</html>
```